Tallowick Limited Business Card

We need a business card for a new company based in Essex, United Kingdom. We develop and manufacture educational games. The business card needs to match the company brand and logo and the colour scheme.
My company makes educational board games to be played by the family or used by teachers
The games are tile based number game

Target Market(s)

Parents, teachers, schools and children

Industry/Entity Type

Games

Contact Information for Business Card

Company Name - Tallowick Limited
Director - Damian Prouse
Registered Office - 3 Marsh Court, 142 Quarry Lane, Brindleford, Essex, CM7 4XR
Phone Number - 07950 000 318
Email - Enquiries@Tallowick.example
Website - www.Tallowick.example
Company Number - 00000000

Font styles to use
Sans Serif

Colors
00a990
ffffff

Requirements
Must have
• Same colour scheme as the attachments - green and white
• Same font style for Tallowick
• Images of the number tiles similar to the attachments
• extra details
• The colour is Cyan - 82 Magenta - 24 Yellow - 44 Black - 2
• I have attached some of the font styles use on my website and alos my LOGO
Nice to have
• Image of the number "1" tag as seen on the website

```html
<!DOCTYPE html>
<html lang="en">
<head>
<meta charset="utf-8">
<title>Tallowick Limited Business Card</title>
<link rel="stylesheet" href="https://fonts.googleapis.com/css2?family=Open+Sans:wght@400;600;700&display=swap">
<style>
  :root {
    --brand-teal: #00a990;
    --ribbon-teal: #1c8b83;
    --ribbon-fold: #0d5b56;
    --deep-green: #0b3f3d;
    --icon-teal: #1fa596;
    --paper: #ffffff;
    --label: #222222;
    --edge: #d9d9d9;
  }
  * { box-sizing: border-box; margin: 0; padding: 0; }
  html, body { width: 1200px; height: 738px; overflow: hidden; background: var(--paper); }
  body { position: relative; font-family: "Open Sans", Arial, sans-serif; }

  .side-label {
    position: absolute; top: 26px; width: 390px; text-align: center;
    font-weight: 700; font-size: 24px; letter-spacing: 1px; color: var(--label);
  }
  .side-label--front { left: 150px; }
  .side-label--back { left: 652px; }

  .card {
    position: absolute; top: 70px; width: 390px; height: 605px;
    background: var(--paper); border: 1px solid var(--edge); overflow: hidden;
  }
  .card--front { left: 150px; }
  .card--back { left: 652px; }

  .company-name {
    position: absolute; left: 0; width: 100%; text-align: center;
    font-family: "Open Sans", Arial, sans-serif; font-weight: 700;
    font-size: 34px; line-height: 1; color: var(--brand-teal);
  }
  .card--front .company-name { top: 188px; }
  .card--back .company-name { top: 112px; }

  .dark-panel { position: absolute; left: 0; width: 100%; bottom: 0; background: var(--deep-green); }
  .card--front .dark-panel { top: 397px; }
  .card--back .dark-panel { top: 250px; }

  .ribbon { position: absolute; left: 28px; width: 334px; }
  .ribbon svg { position: absolute; inset: 0; width: 100%; height: 100%; }
  .ribbon__content {
    position: relative; height: 100%; display: flex; flex-direction: column;
    align-items: center; justify-content: center; color: var(--paper);
  }
  .card--front .ribbon { top: 380px; height: 56px; }
  .card--back .ribbon { top: 232px; height: 68px; }

  .web-line { display: flex; align-items: center; gap: 10px; font-size: 18px; font-weight: 600; margin-top: -8px; }
  .web-line svg { position: static; width: 22px; height: 22px; }

  .person__name { font-size: 25px; font-weight: 700; letter-spacing: 0.5px; line-height: 1; margin-top: -6px; }
  .person__role { font-size: 11px; font-weight: 600; letter-spacing: 0.5px; margin-top: 4px; }

  .tile-art {
    position: absolute; left: 0; bottom: 0; width: 100%; height: 160px;
    background: linear-gradient(180deg, #5f7f84 0%, #a8b9bb 45%, #dbe2e3 100%);
  }

  .contacts { position: absolute; left: 56px; top: 368px; list-style: none; color: var(--paper); }
  .contacts li { display: flex; align-items: flex-start; gap: 18px; font-size: 12.5px; line-height: 1.45; margin-bottom: 18px; }
  .contacts svg { flex: none; width: 16px; height: 16px; margin-top: 2px; }
</style>
</head>
<body>
  <div class="side-label side-label--front">FRONT</div>
  <div class="side-label side-label--back">BACK</div>

  <section class="card card--front">
    <div class="company-name">Tallowick</div>
    <div class="dark-panel"></div>
    <div class="tile-art" role="img" aria-label="Rows of rounded number game tiles with a large number one tile"></div>
    <div class="ribbon">
      <svg viewBox="0 0 334 56" preserveAspectRatio="none" aria-hidden="true">
        <polygon points="0,0 12,48 24,48" fill="var(--ribbon-fold)"/>
        <polygon points="334,0 322,48 310,48" fill="var(--ribbon-fold)"/>
        <polygon points="0,0 334,0 322,48 12,48" fill="var(--ribbon-teal)"/>
      </svg>
      <div class="ribbon__content">
        <div class="web-line">
          <svg viewBox="0 0 24 24" aria-hidden="true">
            <circle cx="12" cy="12" r="11" fill="var(--paper)"/>
            <path d="M12 1v22M1 12h22M4 6c5 2 11 2 16 0M4 18c5-2 11-2 16 0M12 1c-5 5-5 17 0 22M12 1c5 5 5 17 0 22" fill="none" stroke="var(--ribbon-teal)" stroke-width="1.4"/>
          </svg>
          <span>www.Tallowick.example</span>
        </div>
      </div>
    </div>
  </section>

  <section class="card card--back">
    <div class="company-name">Tallowick</div>
    <div class="dark-panel"></div>
    <div class="ribbon">
      <svg viewBox="0 0 334 68" preserveAspectRatio="none" aria-hidden="true">
        <polygon points="0,0 12,60 24,60" fill="var(--ribbon-fold)"/>
        <polygon points="334,0 322,60 310,60" fill="var(--ribbon-fold)"/>
        <polygon points="0,0 334,0 322,60 12,60" fill="var(--ribbon-teal)"/>
      </svg>
      <div class="ribbon__content">
        <div class="person__name">DAMIAN PROUSE</div>
        <div class="person__role">DIRECTOR</div>
      </div>
    </div>
    <ul class="contacts">
      <li>
        <svg viewBox="0 0 16 16" aria-hidden="true"><path d="M8 1a5 5 0 0 0-5 5c0 4 5 9 5 9s5-5 5-9a5 5 0 0 0-5-5z" fill="var(--icon-teal)"/><circle cx="8" cy="6" r="2" fill="var(--deep-green)"/></svg>
        <span>3 Marsh Court, 142 Quarry Lane,<br>Brindleford, Essex, CM7 4XR</span>
      </li>
      <li>
        <svg viewBox="0 0 16 16" aria-hidden="true"><path d="M4 1l3 3-2 2c1 2 3 4 5 5l2-2 3 3-2 3C7 15 1 9 1 3z" fill="var(--icon-teal)"/></svg>
        <span>07950 000 318 / 00000000</span>
      </li>
      <li>
        <svg viewBox="0 0 16 16" aria-hidden="true"><rect x="1" y="3" width="14" height="10" rx="1" fill="var(--icon-teal)"/><path d="M1 4l7 5 7-5" fill="none" stroke="var(--deep-green)" stroke-width="1.2"/></svg>
        <span>Enquiries@Tallowick.example</span>
      </li>
      <li>
        <svg viewBox="0 0 16 16" aria-hidden="true"><circle cx="8" cy="8" r="7" fill="var(--icon-teal)"/><path d="M8 1v14M1 8h14M8 1c-3 3-3 11 0 14M8 1c3 3 3 11 0 14" fill="none" stroke="var(--deep-green)" stroke-width="1"/></svg>
        <span>www.Tallowick.example</span>
      </li>
    </ul>
  </section>
</body>
</html>
```